Create PP presentation that explains the one on one on camera video series that features the world's top real estate developers, builders, investors, banks, lawyers, academics and policy makers. It will be a hard hitting frank discussion about the real issues that the COMMERCIAL (not residential) real estate industry is dealing with. The marketing should be news network looking with high tech look and feel and show that it is provides serious and useful financial news content. We are a commercial real estate firm that has established a media arm to provide REAL TIME information regarding the real estate market place. Examples of look and feel should be KWTAV or Harvelt TV. Two pp have been attached should be able to tell that they are from the same company but encourage to take your own approach. A full pp presentation has been included title Sundial Interviews - make it your own. You do not have to use the same images that were provided, these are just guidelines as to what we want to communicate. The layout can be changed - we are using bullet points but if you have a better way to present the information, please do so.

```html
<!DOCTYPE html>
<html lang="en">
<head>
<meta charset="utf-8">
<title>Sundial Interviews – Slides</title>
<link rel="stylesheet" href="https://fonts.googleapis.com/css2?family=Arimo:wght@400;700&display=swap">
<style>
  :root {
    --page: #ffffff;
    --sky: #18b2ea;
    --sky-deep: #0a96d2;
    --sky-light: #3cc8f5;
    --band: #2cc0f2;
    --rule: #0b6fa3;
    --title: #a4e8fb;
    --white: #ffffff;
    --footer: #bfe9fa;
    --brand: #2fae3b;
    --photo-frame: #1c8fc4;
  }
  * { box-sizing: border-box; margin: 0; padding: 0; }
  html, body { width: 1200px; height: 900px; overflow: hidden; background: var(--page); }
  body { position: relative; font-family: "Arimo", Arial, sans-serif; }

  .slide {
    position: absolute;
    overflow: hidden;
    background:
      radial-gradient(ellipse at 50% 20%, rgba(255,255,255,0.15), transparent 60%),
      linear-gradient(180deg, var(--sky) 0%, var(--sky-deep) 100%);
  }
  .slide--title { left: 201px; top: 33px; width: 818px; height: 461px; }
  .slide--overview { left: 21px; top: 530px; width: 573px; height: 322px; }
  .slide--contact { left: 610px; top: 530px; width: 573px; height: 322px; }

  .band {
    position: absolute; left: 0; right: 0;
    background: linear-gradient(180deg, var(--band), var(--sky-light) 50%, var(--band));
    border-top: 3px solid var(--rule);
    border-bottom: 3px solid var(--rule);
    box-shadow: 0 -14px 24px rgba(4,70,120,0.35), 0 14px 24px rgba(4,70,120,0.35);
    display: flex; align-items: center; justify-content: center;
  }
  .band__title {
    color: var(--title);
    font-weight: 400;
    letter-spacing: 0.09em;
  }
  .slide--title .band { top: 158px; height: 135px; }
  .slide--title .band__title { font-size: 60px; }
  .slide--contact .band { top: 35px; height: 92px; }
  .slide--contact .band__title { font-size: 29px; }

  .overview-header {
    position: absolute; left: 0; right: 0; top: 0; height: 80px;
    border-bottom: 3px solid var(--rule);
    display: flex; align-items: center; padding: 16px 0 0 55px; gap: 12px;
  }
  .overview-header .band__title { font-size: 22px; color: var(--title); }

  .guide-v { position: absolute; left: 12px; top: 92px; width: 1px; height: 204px; background: rgba(255,255,255,0.7); }
  .guide-h { position: absolute; left: 12px; top: 284px; width: 335px; height: 1px; background: rgba(255,255,255,0.7); }

  .points { position: absolute; left: 27px; top: 96px; color: var(--white); list-style: none; letter-spacing: 0.08em; }
  .points__group { font-size: 15px; line-height: 17px; margin-bottom: 16px; }
  .points__group ul { list-style: none; padding-left: 21px; }
  .points__group li { font-size: 11.5px; line-height: 14.5px; }

  .photo {
    position: absolute;
    border: 2px solid var(--photo-frame);
    box-shadow: 0 2px 4px rgba(0,0,0,0.35);
  }

  .footer {
    position: absolute; left: 0; right: 0; bottom: 0; height: 24px;
    background: var(--footer);
    display: flex; align-items: center; padding-left: 13px;
  }
  .brand { color: var(--brand); font-weight: 700; font-size: 12px; letter-spacing: 0.01em; }

  .contact {
    position: absolute; left: 0; right: 0; top: 147px;
    text-align: center; color: var(--white); font-size: 14px; line-height: 21.5px;
  }
</style>
</head>
<body>

  <section class="slide slide--title">
    <div class="band"><h1 class="band__title">Sundial Interviews</h1></div>
  </section>

  <section class="slide slide--overview">
    <header class="overview-header">
      <svg width="42" height="30" viewBox="0 0 42 30" aria-hidden="true">
        <g fill="#ffffff">
          <rect x="0" y="14" width="6" height="16"/>
          <rect x="7" y="8" width="6" height="22"/>
          <rect x="14" y="2" width="6" height="28"/>
          <rect x="21" y="10" width="6" height="20"/>
          <rect x="28" y="5" width="6" height="25"/>
          <rect x="35" y="15" width="7" height="15"/>
        </g>
      </svg>
      <h2 class="band__title">Interviews with Real Estate Icons</h2>
    </header>

    <div class="guide-v"></div>
    <div class="guide-h"></div>

    <ul class="points">
      <li class="points__group">Five Market Segment Series 2014 / 15
        <ul>
          <li>Developers and Builders</li>
          <li>Financial Service Providers</li>
          <li>Legal Practitioners and Scholars</li>
          <li>Brokerage and Technology</li>
          <li>Public Sector</li>
        </ul>
      </li>
      <li class="points__group">Twenty Four Annual Interviews
        <ul>
          <li>Produced bi-weekly</li>
          <li>Content adjusted to market events</li>
        </ul>
      </li>
    </ul>

    <div class="photo" role="img" aria-label="Photo of two engineers in hard hats reviewing a site" style="left:364px;top:88px;width:103px;height:58px;background:linear-gradient(135deg,#8fb6cf,#c9a24a 60%,#56708a);"></div>
    <div class="photo" role="img" aria-label="Photo of high-rise towers under construction" style="left:472px;top:104px;width:83px;height:56px;background:linear-gradient(180deg,#7fb9e6,#b8c6d2 70%,#5d6a75);"></div>
    <div class="photo" role="img" aria-label="Photo of a stone bank facade" style="left:339px;top:150px;width:127px;height:35px;background:linear-gradient(180deg,#8a7a62,#c7b597 50%,#6f604c);"></div>
    <div class="photo" role="img" aria-label="Photo of a judge's gavel on a desk" style="left:469px;top:162px;width:88px;height:60px;background:linear-gradient(135deg,#4a1f0c,#c0621e 55%,#e3a04b);"></div>
    <div class="photo" role="img" aria-label="Digital world map on a blue screen" style="left:384px;top:188px;width:81px;height:57px;background:linear-gradient(135deg,#0b3e86,#1fa6d9 60%,#0a4c9a);"></div>
    <div class="photo" role="img" aria-label="Photo of a domed capitol building" style="left:469px;top:226px;width:100px;height:72px;background:linear-gradient(180deg,#8fb4d8,#e6e6e2 55%,#5b7a3e);"></div>
    <div class="photo" role="img" aria-label="Photo of a red brick university hall among trees" style="left:356px;top:249px;width:108px;height:73px;background:linear-gradient(180deg,#9cc6e6,#8a4030 50%,#3f6a2c);"></div>

    <footer class="footer"><span class="brand">TerraVantix</span></footer>
  </section>

  <section class="slide slide--contact">
    <div class="band"><h2 class="band__title">Contact Information</h2></div>
    <address class="contact" style="font-style:normal;">
      TerraVantix, LLC<br>
      218 N. Larkmoor Avenue, Suite 400<br>
      Brookfield, IL&nbsp; 60513<br>
      (555) 014-2297<br>
      www.terravantix.example
    </address>
    <footer class="footer"><span class="brand">TerraVantix</span></footer>
  </section>

</body>
</html>
```